Stated Income Loans

Flyer design to be used on social media platforms (i.e. Chatterbox, Snapgrove etc.)

Target Market(s)

Real Estate Investors

Requirements
Must have
• INVESTOR STATED INCOME LOANS
• "IT'S TIME TO THINK BIG"
• * Purchase or Refinance up to 3 Million
• * No Income Docs or Bank Statements
• * Vacant Properties Allowed
• * Minimum Credit Score 620
• * Cash Out up to 80%
• Same Day Pre-Approval
• 20-30 Day Close
• Call Marcus Whitfield today...
• Bluecrest Lending Group, Inc.
• Phone (800) 641-2957 x 17
• Direct (240) 958-2074
• www.bluecrestlendhub.com
• NMLS #583617 / #47081
Should not have
• Do not use same color scheme as website. Be creative.

```html
<!DOCTYPE html>
<html lang="en">
<head>
<meta charset="utf-8">
<title>Investor Stated Income Loans – Think Big</title>
<link href="https://fonts.googleapis.com/css2?family=Anton&family=Oswald:wght@500;600;700&family=Open+Sans:wght@400;600;700;800&display=swap" rel="stylesheet">
<style>
  :root {
    --red: #f20000;
    --red-deep: #c40000;
    --yellow: #fff200;
    --cream: #fffbe0;
    --white: #ffffff;
    --ink: #333333;
    --page: #ffffff;
  }
  html, body {
    margin: 0;
    width: 1200px;
    height: 1200px;
    overflow: hidden;
    background: var(--page);
  }
  .flyer {
    position: absolute;
    left: 216px;
    top: 54px;
    width: 832px;
    height: 1076px;
    overflow: hidden;
    background: var(--white);
    font-family: "Open Sans", Arial, sans-serif;
  }
  .burst {
    position: absolute;
    inset: 0 0 auto 0;
    height: 412px;
    background: radial-gradient(ellipse 70% 85% at 70% 38%, var(--white) 0%, var(--cream) 35%, #fff77a 65%, var(--yellow) 100%);
  }
  .investor-photo {
    position: absolute;
    left: 0;
    top: 106px;
    width: 380px;
    height: 306px;
    border-radius: 190px 190px 0 0;
    background: linear-gradient(180deg, #6b4a36 0%, #d9a88a 30%, #e8b89a 70%, #cf9a7c 100%);
  }
  .cash-photo {
    position: absolute;
    left: 444px;
    top: 42px;
    width: 300px;
    height: 232px;
    border-radius: 18px;
    background: linear-gradient(160deg, #eef1e8 0%, #b9c2ae 50%, #7f8a76 100%);
  }
  .headline-lead {
    position: absolute;
    right: 52px;
    top: 338px;
    margin: 0;
    font-family: "Oswald", "Arial Narrow", sans-serif;
    font-weight: 700;
    font-size: 72px;
    line-height: 1;
    color: var(--red);
    white-space: nowrap;
  }
  .hero-band {
    position: absolute;
    left: 0;
    top: 412px;
    width: 832px;
    height: 664px;
  }
  .loan-type {
    position: absolute;
    left: 84px;
    top: 620px;
    width: 712px;
    margin: 0;
    padding-bottom: 4px;
    border-bottom: 1.5px solid var(--red);
    font-family: "Oswald", "Arial Narrow", sans-serif;
    font-weight: 600;
    font-size: 48px;
    letter-spacing: 2.3px;
    line-height: 1.15;
    color: var(--red);
    white-space: nowrap;
  }
  .features {
    position: absolute;
    left: 50px;
    top: 727px;
    margin: 0;
    padding: 0;
    list-style: none;
    width: 330px;
    font-size: 20.5px;
    font-weight: 700;
    color: var(--ink);
    line-height: 35.5px;
  }
  .features li {
    position: relative;
    padding-left: 32px;
  }
  .features li::before {
    content: "";
    position: absolute;
    left: 0;
    top: 14px;
    width: 8px;
    height: 8px;
    border-radius: 50%;
    background: var(--red);
  }
  .contact {
    position: absolute;
    right: 22px;
    top: 700px;
    text-align: right;
    color: var(--white);
  }
  .contact-call {
    margin: 0;
    font-family: "Oswald", "Arial Narrow", sans-serif;
    font-weight: 600;
    font-size: 27px;
    line-height: 1.2;
  }
  .contact-company {
    margin: 4px 0 0;
    font-size: 19px;
    font-weight: 700;
  }
  .contact-direct {
    margin: 14px 0 0;
    font-family: "Oswald", "Arial Narrow", sans-serif;
    font-weight: 500;
    font-size: 50px;
    line-height: 1;
    display: flex;
    align-items: center;
    justify-content: flex-end;
    gap: 10px;
  }
  .contact-direct svg { width: 32px; height: 32px; }
  .contact-office {
    margin: 10px 0 0;
    font-size: 30px;
    line-height: 1.2;
  }
  .contact-web {
    margin: 26px 0 0;
    font-size: 23px;
    font-weight: 700;
    display: flex;
    align-items: center;
    justify-content: flex-end;
    gap: 14px;
  }
  .contact-web svg { width: 36px; height: 36px; }
  .contact-nmls {
    margin: 20px 0 0;
    font-size: 23px;
    font-weight: 700;
  }
</style>
</head>
<body>
<main class="flyer">
  <div class="burst"></div>
  <div class="investor-photo" role="img" aria-label="Photo of a wide-eyed investor peeking up from below"></div>
  <div class="cash-photo" role="img" aria-label="Photo of stacked bundles of hundred-dollar bills in a thought bubble"></div>

  <p class="headline-lead">IT'S TIME TO</p>

  <svg class="hero-band" viewBox="0 0 832 664">
    <defs>
      <linearGradient id="think-fill" x1="0" y1="0" x2="0" y2="1">
        <stop offset="0" stop-color="#ffffff"/>
        <stop offset="0.55" stop-color="#f2f2f2"/>
        <stop offset="1" stop-color="#c9c9c9"/>
      </linearGradient>
    </defs>
    <path d="M0 0 H832 V200 H100 C60 202 25 212 0 222 Z" fill="var(--red)"/>
    <path d="M334 278 H832 V664 H416 C445 580 450 470 440 420 C420 360 380 310 334 278 Z" fill="var(--red)"/>
    <text x="29" y="196" font-family="Anton, Impact, sans-serif" font-size="186" textLength="776" lengthAdjust="spacingAndGlyphs" fill="var(--red-deep)">THINK BIG</text>
    <text x="22" y="190" font-family="Anton, Impact, sans-serif" font-size="186" textLength="776" lengthAdjust="spacingAndGlyphs" fill="url(#think-fill)">THINK BIG</text>
  </svg>

  <h2 class="loan-type">INVESTOR STATED INCOME LOANS</h2>

  <ul class="features">
    <li>Purchase or Refinance up to 3 Million</li>
    <li>No Income Docs or Bank Statements</li>
    <li>Vacant Properties Allowed</li>
    <li>Minimum Credit Score 620</li>
    <li>Cash Out up to 80%</li>
    <li>Same Day Pre-Approval</li>
    <li>20-30 Day Close</li>
  </ul>

  <div class="contact">
    <p class="contact-call">CALL MARCUS WHITFIELD TODAY</p>
    <p class="contact-company">Bluecrest Lending Group, Inc.</p>
    <p class="contact-direct">
      <svg viewBox="0 0 32 32" aria-hidden="true">
        <rect x="1" y="1" width="30" height="30" rx="7" fill="#ffffff"/>
        <path d="M11 7 l4 5 -2 2 c1 3 3 5 6 6 l2 -2 5 4 -2 3 c-8 1 -16 -7 -15 -15 z" fill="var(--red)"/>
      </svg>
      (240)958-2074
    </p>
    <p class="contact-office">(800) 641-2957 x 17</p>
    <p class="contact-web">
      <svg viewBox="0 0 40 40" aria-hidden="true" fill="none" stroke="#ffffff" stroke-width="2">
        <circle cx="20" cy="20" r="17"/>
        <ellipse cx="20" cy="20" rx="8" ry="17"/>
        <line x1="3" y1="20" x2="37" y2="20"/>
        <line x1="20" y1="3" x2="20" y2="37"/>
        <path d="M6 11 H34 M6 29 H34"/>
      </svg>
      www.bluecrestlendhub.com
    </p>
    <p class="contact-nmls">NMLS #583617 / #47081</p>
  </div>
</main>
</body>
</html>
```